Request for Business Card Design

Hi. My name is Marlena, I am looking for a new business card design for my company, Quorvane Sensing Systems, LLC. I really like the design you did for Tessaly Harvest and was hoping you could do something similar using our full logo and our mark. I am also open to any raised texture design using our mark. I have attached our full logo, which would need to be somewhere on the card, as well as the mark in both outline and full form, as well as our brand colors / guide. The card does not have to be white, as long as our logo and mark appear. I actually like darker colored business cards more, but am open to all options. If you are interested in working with me, please let me know. We would also take the business card design into letterhead design if you can do that.

```html
<!DOCTYPE html>
<html lang="en">
<head>
<meta charset="utf-8">
<title>Quorvane Sensing Systems – Business Card</title>
<link href="https://fonts.googleapis.com/css2?family=Open+Sans:ital,wght@0,400;0,600;0,700;0,800&display=swap" rel="stylesheet">
<style>
  :root {
    --page-bg: #2a2a2a;
    --card-bg: #141414;
    --brand-blue: #0e9cc4;
    --text-light: #f2f2f2;
    --text-muted: #d8d8d8;
  }
  * { margin: 0; padding: 0; box-sizing: border-box; }
  html, body {
    width: 1200px;
    height: 900px;
    overflow: hidden;
    background: var(--page-bg);
    font-family: "Open Sans", Arial, sans-serif;
  }
  .stage {
    width: 1200px;
    height: 900px;
    display: flex;
    align-items: center;
    justify-content: center;
  }
  .business-card {
    position: relative;
    width: 1050px;
    height: 600px;
    background: var(--card-bg);
    border-bottom: 6px solid var(--brand-blue);
    overflow: hidden;
    box-shadow: 0 20px 50px rgba(0,0,0,0.5);
  }
  .company-name {
    position: absolute;
    left: 90px;
    top: 60px;
    color: var(--text-light);
    font-weight: 800;
    font-size: 40px;
    letter-spacing: 3px;
    text-transform: uppercase;
    line-height: 1;
  }
  .holder {
    position: absolute;
    left: 60px;
    top: 150px;
    display: flex;
    align-items: flex-start;
  }
  .holder-bar {
    width: 16px;
    height: 58px;
    background: var(--brand-blue);
    margin-right: 24px;
    transform: skewX(-18deg);
  }
  .holder-name {
    color: var(--brand-blue);
    font-weight: 700;
    font-size: 34px;
    text-transform: uppercase;
    line-height: 1.05;
  }
  .holder-title {
    color: var(--text-muted);
    font-size: 22px;
    line-height: 1.4;
  }
  .address {
    position: absolute;
    left: 90px;
    top: 255px;
    color: var(--text-muted);
    font-size: 22px;
    line-height: 1.45;
  }
  .contact-list {
    position: absolute;
    left: 60px;
    top: 355px;
    list-style: none;
    color: var(--text-muted);
    font-size: 22px;
    line-height: 1.55;
  }
  .contact-list li {
    display: flex;
    align-items: center;
    gap: 14px;
  }
  .contact-icon { width: 20px; height: 20px; flex: none; }
  .brand-circle {
    position: absolute;
    right: -120px;
    top: 110px;
    width: 560px;
    height: 560px;
  }
</style>
</head>
<body>
<main class="stage">
  <section class="business-card">
    <h1 class="company-name">Quorvane Sensing Systems</h1>

    <div class="holder">
      <span class="holder-bar"></span>
      <div>
        <p class="holder-name">Dorian Pell</p>
        <p class="holder-title">Managing Director</p>
      </div>
    </div>

    <p class="address">Your address, City<br>State, Zip 1234</p>

    <ul class="contact-list">
      <li>
        <svg class="contact-icon" viewBox="0 0 24 24" aria-hidden="true"><path fill="var(--brand-blue)" d="M6.6 10.8a15.1 15.1 0 0 0 6.6 6.6l2.2-2.2a1 1 0 0 1 1-.25 11.4 11.4 0 0 0 3.6.57 1 1 0 0 1 1 1V20a1 1 0 0 1-1 1A17 17 0 0 1 3 4a1 1 0 0 1 1-1h3.5a1 1 0 0 1 1 1c0 1.25.2 2.45.57 3.6a1 1 0 0 1-.25 1z"/></svg>
        123 456 789
      </li>
      <li>
        <svg class="contact-icon" viewBox="0 0 24 24" aria-hidden="true"><path fill="var(--brand-blue)" d="M2 5h20v14H2z"/><path fill="none" stroke="var(--card-bg)" stroke-width="2" d="M2 5l10 8 10-8"/></svg>
        info@yourmail.com
      </li>
      <li>
        <svg class="contact-icon" viewBox="0 0 24 24" aria-hidden="true"><circle cx="12" cy="12" r="10" fill="var(--brand-blue)"/><path fill="none" stroke="var(--card-bg)" stroke-width="1.5" d="M2 12h20M12 2c3 3 3 17 0 20M12 2c-3 3-3 17 0 20"/></svg>
        www.yourwebsite.com
      </li>
    </ul>

    <svg class="brand-circle" viewBox="0 0 560 560" role="img" aria-label="Brand mark area">
      <circle cx="280" cy="280" r="280" fill="var(--brand-blue)"/>
    </svg>
  </section>
</main>
</body>
</html>
```